Granite Valve Works - Single page line card revamp - new business rebrand

hello,

Our company, KLB (www.klb-harwell.example), just purchased a business, Granite Valve Works (GVW), and we want to revamp their line card to be more modern and use a color scheme similar to KLB's branding. I have attached the existing line card and the GVW logo for the submittal. Please also include their phone number on the brochure: 555-014-7290
I also included a flyer from KLB, as it would also be nice to incorporate the Kinetic Lift & Bearings (KLB) brand into the flyer.

Thanks
Noel

```html
<!DOCTYPE html>
<html lang="en">
<head>
<meta charset="utf-8">
<title>Granite Valve Works – Line Card</title>
<link rel="stylesheet" href="https://fonts.googleapis.com/css2?family=Oswald:wght@400;500;600;700&family=Montserrat:wght@800;900&display=swap">
<style>
  :root{
    --bg:#d4d4d4;
    --paper:#f4f5f7;
    --navy:#1d3a8f;
    --navy-deep:#2a2f7a;
    --royal:#2447a6;
    --sky:#27a7e6;
    --ink:#1f2a5c;
    --text:#3b3f4a;
    --strip:#cdd6ea;
    --rule:#9aa3b5;
    --white:#ffffff;
  }
  *{margin:0;padding:0;box-sizing:border-box}
  html,body{width:1200px;height:900px;overflow:hidden;background:var(--bg)}
  .flyer{position:absolute;left:270px;top:20px;width:660px;height:860px;background:var(--paper);overflow:hidden;box-shadow:0 6px 22px rgba(0,0,0,.18);font-family:'Oswald',sans-serif;color:var(--ink)}
  .hero{position:absolute;left:0;top:0;width:660px;height:420px;
    background:radial-gradient(circle at 22% 55%,rgba(240,138,60,.85) 0,rgba(240,138,60,.25) 22%,transparent 40%),
               linear-gradient(120deg,#c9d3ea 0%,#8d9cc4 35%,#5a6ea8 60%,#b9c6e4 85%,#7e8fbf 100%)}
  .logo-panel{position:absolute;left:0;top:150px;width:330px;height:200px}
  .logo-panel svg{position:absolute;inset:0}
  .brand{position:absolute;left:60px;top:40px;width:230px}
  .brand-row{display:flex;align-items:center;gap:10px}
  .brand-dot{width:30px;height:30px;border-radius:50%;background:var(--royal)}
  .brand-mark{font-size:58px;font-weight:700;line-height:1;color:var(--royal);letter-spacing:2px}
  .brand-name{font-size:15px;font-weight:600;color:var(--royal);letter-spacing:.6px;margin-top:4px}
  .brand-sub{font-size:12px;font-weight:500;color:var(--ink);letter-spacing:3px}
  .band{position:absolute;left:0;top:0;width:660px;height:860px;pointer-events:none}
  .headline{position:absolute;left:36px;top:398px;width:600px;color:var(--white);white-space:nowrap}
  .headline .kicker{font-family:'Montserrat',sans-serif;font-weight:900;font-size:15px;line-height:20px;letter-spacing:1.2px}
  .headline h1{font-size:36px;font-weight:700;line-height:42px;letter-spacing:.3px}
  .subline{position:absolute;left:36px;top:466px;height:34px;line-height:34px;font-size:14px;font-weight:500;color:var(--white);letter-spacing:.4px;white-space:nowrap}
  .offer{position:absolute;left:36px;width:600px;display:grid;grid-template-columns:170px 1fr;column-gap:20px}
  .offer.motors{top:520px}
  .offer.equipment{top:630px}
  .offer h2{font-size:15px;font-weight:600;line-height:1.2;color:var(--ink)}
  .offer .label{font-size:12px;font-weight:500;color:var(--text);margin-top:8px}
  .makers{display:flex;flex-wrap:wrap;gap:4px 12px;align-items:center;padding-bottom:6px;border-bottom:1px solid var(--rule)}
  .maker{display:flex;align-items:center;gap:4px;font-size:11px;line-height:16px;font-weight:600;color:var(--royal);text-transform:uppercase}
  .maker i{width:9px;height:9px;border-radius:50%;background:var(--royal);display:block}
  .services{display:grid;grid-template-columns:repeat(3,1fr);gap:2px 4px;margin-top:6px;list-style:none}
  .services li{font-size:9.5px;color:var(--text);text-transform:uppercase;line-height:1.45}
  .services li::before{content:"• "}
  .strip{position:absolute;left:0;top:748px;width:660px;height:48px;background:var(--strip)}
  .badge{position:absolute;left:36px;top:9px;width:58px;height:30px;border-radius:6px;background:var(--royal)}
  .strip p{position:absolute;left:120px;top:9px;width:510px;font-size:10px;line-height:1.4;color:var(--ink);font-weight:400}
  .footer{position:absolute;left:0;top:796px;width:660px;height:64px;background:var(--navy);color:var(--white)}
  .footer address{position:absolute;left:36px;top:12px;font-style:normal;font-size:11px;line-height:1.35;letter-spacing:.3px}
  .footer address strong{font-weight:600}
  .contact{position:absolute;right:36px;top:9px;text-align:right}
  .phone{font-size:30px;line-height:32px;font-weight:700;letter-spacing:.5px;display:flex;align-items:center;gap:8px;justify-content:flex-end}
  .web{font-size:11px;line-height:14px;letter-spacing:.4px;margin-top:2px}
</style>
</head>
<body>
<main class="flyer">
  <div class="hero" role="img" aria-label="Photo of precision electric motor and machine assembly with warm light flare"></div>

  <svg class="band" viewBox="0 0 660 860" aria-hidden="true">
    <defs>
      <linearGradient id="bandGrad" x1="0" y1="0" x2="1" y2="0">
        <stop offset="0" stop-color="#27a7e6"/>
        <stop offset=".55" stop-color="#2b63c4"/>
        <stop offset="1" stop-color="#2a2f7a"/>
      </linearGradient>
    </defs>
    <polygon points="0,392 660,335 660,468 0,468" fill="url(#bandGrad)"/>
    <rect x="0" y="466" width="660" height="36" fill="#2a2f7a"/>
  </svg>

  <div class="logo-panel">
    <svg viewBox="0 0 330 200" aria-hidden="true"><polygon points="0,0 270,0 330,70 250,200 0,200" fill="#f4f5f7"/></svg>
    <div class="brand">
      <div class="brand-row"><span class="brand-dot"></span><span class="brand-mark">GVW</span></div>
      <div class="brand-name">GRANITE VALVE WORKS</div>
      <div class="brand-sub">A DIVISION OF KLB</div>
    </div>
  </div>

  <header class="headline">
    <p class="kicker">WE PROVIDE PROMPT, QUALITY SALES AND SERVICE</p>
    <h1>OF NEW AND USED ELECTRIC MOTORS.</h1>
  </header>
  <p class="subline">WE MAINTAIN LARGE INVENTORIES IN ORDER TO BETTER SERVICE OUR VALUED CUSTOMERS</p>

  <section class="offer motors">
    <div>
      <h2>NEW MOTOR SALES FOR<br>THESE BRANDS AND MORE:</h2>
      <p class="label">Other Services Include:</p>
    </div>
    <div>
      <div class="makers">
        <span class="maker"><i></i>Tarnwell</span>
        <span class="maker">Orvane</span>
        <span class="maker">Kestrel Drives</span>
        <span class="maker">Pellor</span>
        <span class="maker">Brandt Motors</span>
        <span class="maker">Orvane</span>
        <span class="maker"><i></i>Ridgeway Electric</span>
      </div>
      <ul class="services">
        <li>Electric motor repairing</li>
        <li>Process pump repair</li>
        <li>Vibration analysis</li>
        <li>PD &amp; centrifugal blower repair</li>
        <li>Vertical turbine pump repair</li>
        <li>Hydraulic repair</li>
        <li>Laser alignments</li>
      </ul>
    </div>
  </section>

  <section class="offer equipment">
    <div>
      <h2>WE ALSO PROVIDE NEW<br>PROCESS EQUIPMENT FOR<br>THESE BRANDS AND MORE:</h2>
      <p class="label">Additional Services Included:</p>
    </div>
    <div>
      <div class="makers">
        <span class="maker"><i></i>Corvane Pumps</span>
        <span class="maker">Meterline</span>
        <span class="maker">Hollis Pump</span>
        <span class="maker"><i></i>Brightflow</span>
        <span class="maker">Lorimer</span>
        <span class="maker">Stavro</span>
        <span class="maker">Halden</span>
        <span class="maker">Nordvik</span>
      </div>
      <ul class="services">
        <li>Control panel design</li>
        <li>Roots type blower packages</li>
        <li>Automation / SCADA support</li>
        <li>Booster skid fabrication</li>
      </ul>
    </div>
  </section>

  <section class="strip">
    <span class="badge" aria-hidden="true"></span>
    <p>We are proud members of RMSA and adhere to their high standards. Our competent staff is available 24 hours a day to assist you with your needs for motors, pumps and related equipment.</p>
  </section>

  <footer class="footer">
    <address>
      <strong>GRANITE VALVE WORKS</strong><br>
      88 Quarry Mill Road Harwell, VA 20417<br>
      SERVICE@GVW-KLB.EXAMPLE
    </address>
    <div class="contact">
      <div class="phone">
        <svg width="20" height="20" viewBox="0 0 24 24" aria-hidden="true"><path fill="#ffffff" d="M6.6 10.8a15.1 15.1 0 0 0 6.6 6.6l2.2-2.2c.3-.3.7-.4 1-.2 1.1.4 2.3.6 3.6.6.6 0 1 .4 1 1V20c0 .6-.4 1-1 1A17 17 0 0 1 3 4c0-.6.4-1 1-1h3.5c.6 0 1 .4 1 1 0 1.3.2 2.5.6 3.6.1.3 0 .7-.2 1z"/></svg>
        555-014-7290
      </div>
      <div class="web">www.gvw-klb.example</div>
    </div>
  </footer>
</main>
</body>
</html>
```